Business Card Re-Design for a Lighting Designer

I would like my business card re-designed. It is currently high gloss and they scratch too easily. I don not think the current design lends itself well to a matte finish. I have included the current design for reference along with our company logo.
Check out our website for current branding.
http://www.brambleorchidstudio.example

Updates
Some of the top contenders are muslim and it is a holiday for them. I do not want to discriminate and would expect the same courtesy for holidays we celebrate.
Target Market(s)
Interior Designers, Architects
Contact Information for Business Card
Logo - Name, Title, Address, Telephone Number and Extension, Email
Font styles to use
Requirements
Must have
- All the information listed on the current business card. If you use Red, it needs to be the red from our logo.
Nice to have
- Vertical and Horizontal Designs will be entertained.
Should not have
- Requirements for a glossy finish...should not look too corporate since we are a design firm.

```html
<!DOCTYPE html>
<html lang="en">
<head>
<meta charset="utf-8">
<title>Bramble Orchid Studio — Business Card</title>
<link href="https://fonts.googleapis.com/css2?family=Lato:wght@400;700&display=swap" rel="stylesheet">
<style>
  :root {
    --brand-red: #990000;
    --charcoal: #232325;
    --ink: #2a2a2a;
    --paper: #ffffff;
    --backdrop: #141414;
    --muted: #8a8a8a;
  }
  * { margin: 0; padding: 0; box-sizing: border-box; }
  html, body { width: 1200px; height: 912px; overflow: hidden; }
  body {
    background: var(--backdrop);
    font-family: "Lato", sans-serif;
    position: relative;
  }
  .card {
    position: absolute;
    left: 250px;
    width: 700px;
    height: 400px;
    overflow: hidden;
  }
  .card--front { top: 40px; background: var(--charcoal); }
  .card--back { top: 472px; background: var(--paper); }

  .wordmark {
    display: flex;
    align-items: center;
    gap: 14px;
    font-weight: 400;
    letter-spacing: 1px;
    line-height: 1.05;
    text-transform: uppercase;
  }
  .wordmark__square {
    width: 58px; height: 58px;
    background: var(--brand-red);
    flex: none;
  }
  .card--front .wordmark {
    position: absolute; left: 50%; top: 118px;
    transform: translateX(-50%);
    color: var(--paper);
    font-size: 34px;
  }
  .card--front .site {
    position: absolute; left: 0; right: 0; bottom: 52px;
    text-align: center;
    color: var(--paper);
    font-size: 20px;
    letter-spacing: 0.5px;
  }

  .card--back .wordmark {
    position: absolute; left: 48px; top: 70px;
    color: var(--ink);
    font-size: 28px;
  }
  .person {
    position: absolute; right: 56px; top: 44px;
    text-align: right;
  }
  .person__name { color: var(--brand-red); font-weight: 700; font-size: 24px; }
  .person__title { color: var(--ink); font-size: 16px; margin-top: 2px; }
  .rule {
    position: absolute; left: 48px; right: 56px; top: 186px;
    height: 2px; background: var(--brand-red);
  }
  .contact {
    position: absolute; left: 48px; top: 214px;
    list-style: none;
    color: var(--ink); font-size: 18px;
  }
  .contact li { display: flex; align-items: center; gap: 12px; margin-bottom: 10px; }
  .contact svg { width: 18px; height: 18px; fill: var(--brand-red); flex: none; }
  .address {
    position: absolute; right: 56px; top: 204px;
    text-align: right; color: var(--ink); font-size: 17px; line-height: 1.45;
    font-style: normal;
  }
  .swoosh { position: absolute; left: 0; bottom: 0; width: 700px; height: 140px; }
  .card--back .site {
    position: absolute; right: 28px; bottom: 18px;
    color: var(--paper); font-size: 17px;
  }
</style>
</head>
<body>
  <section class="card card--front">
    <div class="wordmark"><span class="wordmark__square"></span><span>Bramble Orchid<br>Studio</span></div>
    <p class="site">www.brambleorchidstudio.example</p>
  </section>

  <section class="card card--back">
    <div class="wordmark"><span class="wordmark__square"></span><span>Bramble Orchid<br>Studio</span></div>
    <div class="person">
      <p class="person__name">Maren Holloway</p>
      <p class="person__title">Principal</p>
    </div>
    <div class="rule"></div>
    <ul class="contact">
      <li><svg viewBox="0 0 24 24"><path d="M6.6 10.8a15.1 15.1 0 0 0 6.6 6.6l2.2-2.2a1 1 0 0 1 1-.25 11.4 11.4 0 0 0 3.6.57 1 1 0 0 1 1 1V20a1 1 0 0 1-1 1A17 17 0 0 1 3 4a1 1 0 0 1 1-1h3.5a1 1 0 0 1 1 1c0 1.25.2 2.45.57 3.57a1 1 0 0 1-.25 1z"/></svg>555.014.2290 x1</li>
      <li><svg viewBox="0 0 24 24"><path d="M2 5h20v14H2z M3 6l9 7 9-7" stroke="#fff" stroke-width="1.5"/></svg>maren@brambleorchidstudio.example</li>
    </ul>
    <address class="address">412 Alder Grove Lane, Suite 130<br>Springfield, Oregon 97477 USA</address>
    <svg class="swoosh" viewBox="0 0 700 140" preserveAspectRatio="none" aria-hidden="true">
      <path d="M330 140 C430 90 560 60 700 30 L700 140 Z" fill="var(--charcoal)"/>
      <path d="M300 140 C420 85 560 50 640 38 C540 60 430 95 345 140 Z" fill="var(--brand-red)"/>
    </svg>
    <p class="site">www.brambleorchidstudio.example</p>
  </section>
</body>
</html>
```